依頼詳細
いまあるサンプルを春らしく変えて頂いても結構ですし、違うイメージで一から作成して頂いても結構です。このサンプルデザインに特にこだわりがあるわけではありませんので、良いデザインがあればどんどんご提案下さい。

対象が女性の50代~70代になるのでデザインのおしゃれさも大事ですが、シンプルでわかりやすいデザインを希望します。

A3サイズとB4サイズで作成をして下さい。
内容はまったく同じで用紙に合わせてレイアウトを調整して下さい。

真ん中部分の広告商品の商品名や価格はダミーで入れて頂ければ後から私が加筆します。

今後は季節ごとに配色を変えたり、季節感のある物を軽く挿入する程度で、作って頂いたデザインを通年使用していく予定です。

2ヶ月ごとに新聞広告の作成がありますので、今後ともよろしくお願いします。

選択させて頂いた広告の著作権(財産権)等は当方に譲渡をお願いします。フォントや画像素材などを利用する場合は上記利用用途に使用できることを確認し、第三者の知的財産権等に注意して下さい。
記載項目
会期 4月5日(火)~10日(日)

営業時間 10:00~18:00(最終日のみ15:00迄)

会場 アサギリモール一階・北側 SPACEはなゆき 京都市北区雲井南梅枝町38-6

主催 株式会社明葉 京都市北区雲井西竹丘町17-42 tel075-555-0183

2015年4月のサンプルにあるネットショップとブログの案内は省いて下さい。
サイズ
A3
ページ数
片面
希望イメージ
シンプル 複雑
単色 カラフル
暗い 明るい
日常 高級
遊び心 厳粛
未来的 伝統的
女性的 男性的
希望する色
納品ファイル
• 高解像度JPG (.jpg)
• イラストレーター形式 (.ai)
• フォトショップ形式 (.psd)
補足説明
サンプルを添付をさせて頂きます
たくさんのすばらしいデザインを作成して頂き、皆様本当にありがとうございます。

良いデザインばかりなので選定作業が困難を極めています(笑)

採用させて頂いた方はもちろん、それ以外の方も今後ともよろしくお願い申し上げます。

ありがとうございました。
■ 選んだ理由

女性のデザイナーさんらしくやさしさが伝わってきました。

■ 提案者全員のお礼・コメント

皆様本当にありがとうございました。明葉の広告をこんなたくさんの方にデザインしていただきうれしく思います。今後もよろしくお願いします。

```html
<!DOCTYPE html>
<html lang="ja">
<head>
<meta charset="utf-8">
<title>明葉の婦人服 春祭り</title>
<link rel="stylesheet" href="https://fonts.googleapis.com/css2?family=Noto+Sans+JP:wght@500;700;900&family=Noto+Serif+JP:wght@700;900&display=swap">
<style>
  :root{
    --pink-deep:#d6336f;
    --pink-dark:#b8245a;
    --pink-mid:#ec7fa5;
    --pink-soft:#f8d3e0;
    --pink-pale:#fdeef3;
    --white:#ffffff;
    --ink:#4a2a35;
  }
  *{margin:0;padding:0;box-sizing:border-box}
  html,body{width:847px;height:1200px;overflow:hidden;background:var(--white)}
  .poster{position:relative;width:847px;height:1200px;overflow:hidden;
    background:linear-gradient(180deg,var(--pink-soft) 0%,var(--pink-pale) 45%,#fff7fa 100%);
    font-family:"Noto Sans JP",sans-serif;color:var(--ink)}
  .blossoms{position:absolute;left:0;top:0;width:847px;height:880px;
    background:radial-gradient(circle at 12% 40%,rgba(236,127,165,.35),transparent 28%),
               radial-gradient(circle at 90% 30%,rgba(236,127,165,.3),transparent 25%),
               radial-gradient(circle at 15% 78%,rgba(236,127,165,.25),transparent 22%),
               radial-gradient(circle at 88% 72%,rgba(236,127,165,.25),transparent 22%)}
  .brand{position:absolute;left:28px;top:0;width:250px;height:100px;background:var(--white);
    display:flex;align-items:center;justify-content:center;gap:10px}
  .brand-dot{width:14px;height:14px;border-radius:50%;background:var(--pink-deep)}
  .brand-name{font-family:"Noto Sans JP",sans-serif;font-weight:900;font-size:34px;letter-spacing:3px;color:var(--pink-deep)}
  .banner{position:absolute;right:28px;top:8px;width:440px;height:108px;background:var(--pink-deep);
    color:var(--white);font-family:"Noto Serif JP",serif;font-weight:900;font-size:30px;line-height:46px;
    display:flex;flex-direction:column;justify-content:center;padding-left:36px}
  .headline{position:absolute;left:0;width:847px;text-align:center;color:var(--pink-dark);
    font-family:"Noto Sans JP",sans-serif;font-weight:900;font-size:86px;top:132px;letter-spacing:4px}
  .title{position:absolute;left:0;width:847px;text-align:center;top:210px;
    font-family:"Noto Serif JP",serif;font-weight:900;font-size:200px;letter-spacing:6px;line-height:1.2;
    color:var(--pink-deep);text-shadow:4px 4px 0 var(--white)}
  .tagline{position:absolute;left:0;width:847px;text-align:center;top:497px;
    font-family:"Noto Serif JP",serif;font-weight:700;font-size:25px;color:var(--pink-dark)}
  .tags{position:absolute;left:30px;top:548px;width:787px;display:grid;
    grid-template-columns:repeat(3,240px);column-gap:33px;row-gap:32px}
  .tag{position:relative;height:118px;background:var(--white);
    clip-path:polygon(22px 0,100% 0,100% 100%,22px 100%,0 50%);
    display:flex;flex-direction:column;justify-content:center;padding-left:44px}
  .tag::before{content:"";position:absolute;left:18px;top:52px;width:14px;height:14px;border-radius:50%;
    border:2px solid var(--pink-mid)}
  .tag-code{font-size:28px;font-weight:700;letter-spacing:2px;color:var(--ink)}
  .tag-price{display:flex;align-items:flex-end;gap:8px}
  .tag-num{font-size:54px;font-weight:900;line-height:1;color:var(--ink)}
  .tag-unit{font-size:13px;font-weight:700;line-height:1.2;writing-mode:vertical-rl;color:var(--ink)}
  .info{position:absolute;left:34px;top:880px;width:430px;font-family:"Noto Serif JP",serif;font-weight:900;color:var(--ink)}
  .info-row{display:flex;align-items:flex-start;gap:10px}
  .info-label{background:var(--pink-deep);color:var(--white);font-size:20px;padding:6px 5px;line-height:1.1;writing-mode:vertical-rl}
  .date{font-size:32px;line-height:48px}
  .hours{font-size:44px;line-height:52px;margin-left:52px}
  .hours-note{font-size:24px;margin-left:52px;line-height:34px}
  .venue{margin-top:10px}
  .venue-name{font-size:33px;line-height:42px}
  .venue-addr{font-size:21px;margin-left:52px;margin-top:4px}
  .map-wrap{position:absolute;left:490px;top:885px;width:327px;height:230px;border:3px solid var(--pink-mid);background:var(--white)}
  .map-label{position:absolute;left:50%;top:-16px;transform:translateX(-50%);background:var(--pink-mid);color:var(--white);
    font-size:17px;font-weight:700;padding:2px 16px;border-radius:14px}
  .map{position:absolute;left:10px;top:22px;right:10px;bottom:10px;background:linear-gradient(135deg,#f4f1f2,#e6dfe2)}
  .footer{position:absolute;left:0;top:1140px;width:847px;text-align:center;font-size:17px;font-weight:500;color:var(--ink)}
</style>
</head>
<body>
<div class="poster">
  <div class="blossoms" role="img" aria-label="桜の花の装飾"></div>

  <div class="brand"><span class="brand-dot"></span><span class="brand-name">SERENA</span></div>
  <div class="banner"><span>春物、夏物、特別価格!</span><span>今回もお値打ち品多数!</span></div>

  <h2 class="headline">明葉の婦人服</h2>
  <h1 class="title">春祭り</h1>
  <p class="tagline">品質・価格に自信をもって取り揃えております。ご期待ください。</p>

  <div class="tags">
    <div class="tag"><span class="tag-code">00000000</span><div class="tag-price"><span class="tag-num">0000</span><span class="tag-unit">本体円</span></div></div>
    <div class="tag"><span class="tag-code">00000000</span><div class="tag-price"><span class="tag-num">0000</span><span class="tag-unit">本体円</span></div></div>
    <div class="tag"><span class="tag-code">00000000</span><div class="tag-price"><span class="tag-num">0000</span><span class="tag-unit">本体円</span></div></div>
    <div class="tag"><span class="tag-code">00000000</span><div class="tag-price"><span class="tag-num">0000</span><span class="tag-unit">本体円</span></div></div>
    <div class="tag"><span class="tag-code">00000000</span><div class="tag-price"><span class="tag-num">0000</span><span class="tag-unit">本体円</span></div></div>
    <div class="tag"><span class="tag-code">00000000</span><div class="tag-price"><span class="tag-num">0000</span><span class="tag-unit">本体円</span></div></div>
  </div>

  <div class="info">
    <div class="info-row"><span class="info-label">会期</span><span class="date">4月5日(火)~10日(日)</span></div>
    <div class="hours">10:00~18:00</div>
    <div class="hours-note">(最終日のみ15:00まで)</div>
    <div class="info-row venue"><span class="info-label">会場</span><span class="venue-name">アサギリモール一階・<br>北側 SPACEはなゆき</span></div>
    <div class="venue-addr">京都市北区雲井南梅枝町38-6</div>
  </div>

  <div class="map-wrap">
    <span class="map-label">周辺地図</span>
    <div class="map" role="img" aria-label="会場周辺の地図"></div>
  </div>

  <p class="footer">主催 株式会社明葉 京都市北区雲井西竹丘町17-42 TEL 075-555-0183 http://meiyou-fashion.jp/</p>
</div>
</body>
</html>
```